Spice Business needs a packaging design

Creative Brief Document

Project Name – Spice & Seasoning blends

Project brief summary
- Brief summary of the project
We are excited to launch a new spice company called “Meadow’s Own,” dedicated to providing sustainably sourced, high-quality spices and spice blends. We are currently exploring packaging materials for PET jars and gift bundle boxes.
The visual identity should convey a sense of purity, earthiness, vibrancy, and gourmet appeal, capturing the essence of spices while ensuring a global appeal.

Products

All Purpose Seasoning
Curry Powder
Beef Bouillon
Chicken Bouillon
Garlic & Herb
Jollof Rice
Seasoning Salt

Jar & Lid Details (see attached files)

- Reason behind brand name

“Meadow’s Own” name to communicate pure, natural and REAL product.

- What are your business goals?
To show
1. authenticity of product - Pure & High-quality spices with no additives
2. Eco-consiousness (sustainability)
3. Vibrancy - Naturally rich and flavourful
4. Breath of fresh air
5. Exciting product
6. Premium product, yet accessible
7. Gain consumer confidence around transparency/honesty
8. Gain market share from established competitors, with a strong market leader for many years
9. Global market address

Target audience?

Mass market & Institutions (Hotels, restaurants etc)
Gift boxes for holidays such as Christmas

Brand positioning?
- Price point? Premium?
Accessible

Tone of Voice
- Eg friendly, fun, professional, expert, eco conscious, etc?

Tone to be elegant, vibrant and align with the idea of authenticity (realness), health and sustainability, just as nature intended it to be.

Modern, Classy and appealing to display in shelves despite the variety of kitchen decors
Pure and Fresh
Vibrant & Flavourful

Crisp labels when printed out

Competitors
- main competition?

Coastal Ember https://www.coastalembergroup.example/
Kivu Pantry https://www.kivupantryea.example/our-brands/kivu-pantry
Vital Mo https://www.vitalmo.example/product-category/foods/

- Which brands are already out there doing a similar thing?

I like global brands such as Lorvo, Pellam’s, Van Drossel, Ashgrove Pure Salt etc

- How to stand out?

Attractive packaging

What are your key messages?
- What is the key idea the pack needs to communicate?

Real product (Authentic)
Fresh
Accessible
Beautiful
Easy to use

- Do you have a unique selling point?

100% Natural (No additives or fillers)
Sustainably sourced
Premium quality at an accessible price
Eco-friendly packaging

Packaging
- Preferred packaging structure?

**We are using pet jars to package all our products for now.
We would like a label that goes round the jar and also with a tamper seal that goes over the lid .

See these video:

Apply labels with tamper seals on Valdon Works' TableTRAK label applicator (vidstream.example)

Brand Name: Meadow’s Own with logo

Unique Selling Point/ Tags: ALL Natural, No preservatives, Premium Quality

Product Name: Chicken Seasoning
(Ladha ya Bata)

Product Picture: Stock pics
 Compact jar, more spice – less plastic waste! 🌍
 Heat levels: visual icons for 0-All flavor, No heat, 1- Mild, 2-Medium, 3-Hot
• Scan for delicious recipes: QR code for recipes
• Enjoy on: [list] Chicken, Seafood, xx, etc
• Symbols to add: Recycling, Sustainability, Eco-Friendly (Better for the environment), Low Carbon Footprint, Suitable for Vegetarians, NQAs Mark of Standardization, Product Barcode, Kenyan Flag (Made in Kenya)

Product Details:
• Ingredients: xxx
• Nutritional Facts
 About xx servings per container
 Serving size x tbsp. (x g)
 Calories per serving x
• Allergen Information
• Net wt.: g and oz – Make this section extremely visible

Company Details:

Willowgate Harvest Co. Ltd
P.O. Box 42615, GPO 00300
Nairobi, Kenya
Tel: 07xxxxxxxx
www.willowgateharvest.example

Storage Details:
Store in a cool and dry place

Target Market(s)

Mass market with a global appeal

Industry/Entity Type

Spices and Seasonings

Colors

Designer to choose colors to be used in the design.

Requirements
Must have
• colourful, quick to read at a glance pics and fonts. Minimal details in the front i.e. logo, spice name, heat levels, weight & centre picture
Should not have
• Hard to easily read fonts

```html
<!DOCTYPE html>
<html lang="en">
<head>
<meta charset="utf-8">
<title>Meadow’s Own — All Purpose Seasoning Label</title>
<link rel="stylesheet" href="https://fonts.googleapis.com/css2?family=Oswald:wght@400;500;700&display=swap">
<style>
  :root {
    --page: #f2f0ec;
    --wood-light: #d8c2ad;
    --wood-mid: #c4a78e;
    --wood-dark: #a98a72;
    --art-zone: rgba(120, 92, 70, 0.18);
    --panel: #0c0c0c;
    --panel-edge: #2a2a2a;
    --frame: #f4f4f4;
    --banner: #ee3240;
    --banner-dark: #d9222f;
    --gold: #fcd21c;
    --white: #ffffff;
    --flourish: #e2333b;
  }
  * { box-sizing: border-box; margin: 0; padding: 0; }
  html, body {
    width: 900px; height: 1200px; overflow: hidden;
    background: var(--page);
    font-family: "Oswald", sans-serif;
  }
  .label {
    position: absolute; left: 40px; top: 108px;
    width: 820px; height: 984px;
    background:
      radial-gradient(ellipse at 50% 40%, rgba(255,255,255,.25), transparent 60%),
      linear-gradient(100deg, var(--wood-mid), var(--wood-light) 35%, var(--wood-mid) 60%, var(--wood-light) 85%, var(--wood-dark));
    overflow: hidden;
  }
  .art-zone {
    position: absolute;
    background: var(--art-zone);
    border-radius: 8px;
  }
  .art-zone--top-left { left: 60px; top: 20px; width: 230px; height: 170px; }
  .art-zone--left { left: 12px; top: 250px; width: 100px; height: 330px; }
  .art-zone--right { left: 712px; top: 90px; width: 96px; height: 600px; }
  .art-zone--bottom-left { left: 30px; top: 720px; width: 160px; height: 150px; }
  .art-zone--bottom-right { left: 630px; top: 750px; width: 150px; height: 150px; }
  .art-zone--bottom { left: 240px; top: 852px; width: 240px; height: 110px; }

  .panel {
    position: absolute; left: 120px; top: 146px;
    width: 586px; height: 706px;
    background: linear-gradient(180deg, var(--panel-edge), var(--panel) 25%);
  }
  .panel__frame {
    position: absolute; inset: 28px 22px 18px 22px;
    border: 2px solid var(--frame);
  }
  .brand-banner {
    position: absolute; left: 44px; top: 64px;
    width: 498px; height: 128px;
    background: linear-gradient(90deg, var(--banner-dark), var(--banner) 50%, var(--banner-dark));
    display: flex; align-items: center; justify-content: center;
  }
  .brand-banner__name {
    font-weight: 500; font-size: 54px; letter-spacing: 2px;
    color: var(--white); text-transform: uppercase; line-height: 1;
  }
  .product-name {
    position: absolute; left: 0; right: 0; top: 228px;
    text-align: center; color: var(--gold);
    font-weight: 700; font-size: 92px; line-height: 1.06;
    text-transform: uppercase; letter-spacing: 1px;
  }
  .divider {
    position: absolute; left: 78px; top: 460px; width: 430px; height: 40px;
  }
  .tagline {
    position: absolute; left: 0; right: 0; top: 530px;
    text-align: center; color: var(--white);
    font-weight: 500; font-size: 32px; line-height: 1.2;
    text-transform: uppercase;
  }
  .net-weight {
    position: absolute; left: 0; right: 0; top: 620px;
    text-align: center; color: var(--gold);
    font-weight: 700; font-size: 32px;
  }
</style>
</head>
<body>
  <main class="label">
    <div class="art-zone art-zone--top-left" role="img" aria-label="Illustration of red bell peppers"></div>
    <div class="art-zone art-zone--left" role="img" aria-label="Illustrations of a green chilli and carrots"></div>
    <div class="art-zone art-zone--right" role="img" aria-label="Illustrations of a beetroot, pea pods and onions"></div>
    <div class="art-zone art-zone--bottom-left" role="img" aria-label="Illustration of aubergines"></div>
    <div class="art-zone art-zone--bottom-right" role="img" aria-label="Illustration of mushrooms"></div>
    <div class="art-zone art-zone--bottom" role="img" aria-label="Illustration of tomatoes"></div>

    <section class="panel">
      <div class="panel__frame"></div>
      <div class="brand-banner">
        <span class="brand-banner__name">Meadow’s Own</span>
      </div>
      <h1 class="product-name">All Purpose<br>Seasoning</h1>
      <svg class="divider" viewBox="0 0 430 40" aria-hidden="true">
        <path d="M10 22 Q215 -4 420 22" fill="none" stroke="var(--flourish)" stroke-width="3"/>
        <path d="M60 30 Q215 14 370 30" fill="none" stroke="var(--flourish)" stroke-width="2"/>
      </svg>
      <p class="tagline">Perfectly blended with<br>natural paprika and onion</p>
      <p class="net-weight">50gm NET</p>
    </section>
  </main>
</body>
</html>
```